Veterinary TPLO Surgery Flyer Design

Please use this flyer to make a professional-looking 1 page, double-sided client handout regarding TPLO.

You can visit our website at www.brookferrypetcare.com & www.northgroveanimalsurgery.com for additional logo information. The flyer should include all the text from the one provided.

Target Market(s)

Client communication to for referral surgery between sister veterinary clinics

Industry/Entity Type

Veterinary

Requirements
Must have
• The text included
Nice to have
• Nice to have the Willow Crest Avenue Animal CLinic & Dr. Pettigrew Mobile vet logos incorporated.

```html
<!DOCTYPE html>
<html lang="en">
<head>
<meta charset="utf-8">
<title>TPLO Surgery Handout – Willow Crest Avenue Animal Clinic</title>
<link href="https://fonts.googleapis.com/css2?family=Montserrat:wght@300;400;500;600;700;800&display=swap" rel="stylesheet">
<style>
  :root {
    --green: #3f7b57;
    --green-dark: #336848;
    --ink: #1d1d1d;
    --paper: #ffffff;
    --bg: #3a3a3a;
  }
  * { box-sizing: border-box; margin: 0; padding: 0; }
  html, body { width: 889px; height: 1200px; overflow: hidden; background: var(--bg); }
  body { font-family: "Montserrat", sans-serif; color: var(--ink); position: relative; }

  .page { position: absolute; top: 305px; width: 656px; height: 922px; background: var(--paper); overflow: hidden; transform: scale(0.64); transform-origin: 0 0; box-shadow: 0 6px 18px rgba(0,0,0,0.45); }
  .page-front { left: 16px; }
  .page-back { left: 453px; }

  .block { position: absolute; }
  h2 { color: var(--green); font-size: 19px; font-weight: 700; line-height: 1.08; margin-bottom: 6px; }
  p { font-size: 10.6px; line-height: 1.38; font-weight: 500; }

  /* front */
  .masthead { left: 0; top: 0; width: 656px; height: 95px; background: var(--green); display: flex; align-items: center; }
  .brand { width: 233px; height: 100%; display: flex; align-items: center; justify-content: center; gap: 7px; border-right: 2px solid var(--paper); color: var(--paper); }
  .brand-mark { width: 22px; height: 22px; background: var(--paper); border-radius: 50%; flex: none; }
  .brand-name { display: flex; flex-direction: column; line-height: 1.1; }
  .brand-name .line1 { font-size: 13px; font-weight: 500; }
  .brand-name .line2 { font-size: 21px; font-weight: 300; }
  .masthead-title { padding: 0 20px; color: var(--paper); font-size: 12.4px; font-weight: 800; line-height: 1.55; text-transform: uppercase; }

  .about { left: 27px; top: 104px; width: 602px; }
  .about p { text-align: justify; }
  .what { left: 27px; top: 214px; width: 302px; }
  .benefits { left: 346px; top: 214px; width: 290px; }
  .benefit { display: flex; gap: 14px; margin-bottom: 9px; }
  .benefit svg { flex: none; width: 42px; height: 42px; margin-top: 2px; }
  .benefit h3 { font-size: 12.4px; font-weight: 700; line-height: 1.1; }
  .benefit p { font-size: 10.4px; line-height: 1.3; }
  .why { left: 346px; top: 434px; width: 285px; }
  .why p + p { margin-top: 14px; }

  .knee-illustration { left: 26px; top: 355px; width: 290px; height: 250px; background: linear-gradient(135deg, #c9c7c1, #eeeadd 55%, #b9b7b3); }
  .radiograph { left: 26px; top: 613px; width: 290px; height: 252px; background: linear-gradient(180deg, #2a2a2a, #111 60%, #3a3a3a); }
  .pet-photo-front { left: 346px; top: 667px; width: 112px; height: 195px; background: radial-gradient(ellipse at 55% 45%, #5b3e30, #8b7a6a 55%, #ffffff 80%); }

  .footer { left: 0; bottom: 0; width: 656px; height: 47px; background: var(--green); display: flex; align-items: center; gap: 22px; padding-left: 26px; color: var(--paper); font-size: 10.6px; font-weight: 500; }
  .footer span { display: flex; align-items: center; gap: 6px; }
  .footer svg { width: 12px; height: 12px; }

  .surgeon-badge { left: 500px; top: 782px; width: 124px; height: 120px; background: var(--paper); display: flex; flex-direction: column; align-items: center; justify-content: center; gap: 6px; }
  .surgeon-badge .dot { width: 18px; height: 18px; border-radius: 50%; background: var(--green); }
  .surgeon-badge .name { font-size: 12px; font-weight: 700; color: var(--green-dark); }

  /* back */
  .radiograph-note { left: 0; top: 0; width: 656px; height: 112px; background: var(--green); color: var(--paper); padding: 26px 24px 0; }
  .radiograph-note h3 { font-size: 11.4px; font-weight: 700; line-height: 1.2; }
  .radiograph-note p { font-size: 10.4px; line-height: 1.3; }
  .process { left: 24px; top: 126px; width: 610px; }
  .process ol { padding-left: 16px; font-size: 10.4px; font-weight: 500; line-height: 1.25; }
  .process li { margin-bottom: 5px; padding-left: 2px; }
  .followup { left: 22px; top: 370px; width: 612px; }
  .followup .lead { font-weight: 700; margin-bottom: 6px; }
  .followup .visit { padding-left: 16px; margin-bottom: 5px; }
  .followup .closing { margin-top: 12px; }
  .contact-title { left: 0; top: 508px; width: 656px; text-align: center; font-size: 17px; font-weight: 500; }
  .contact-card { top: 545px; width: 296px; height: 250px; background: var(--green); border-radius: 20px; color: var(--paper); padding: 22px 24px; }
  .contact-card h4 { font-size: 16px; font-weight: 600; line-height: 1.2; text-align: center; margin-bottom: 16px; }
  .contact-card p { font-size: 12px; font-weight: 400; line-height: 1.5; margin-bottom: 12px; }
  .card-clinic { left: 22px; }
  .card-clinic p { padding-left: 16px; }
  .card-surgeon { left: 331px; }
  .pet-photo-back { left: 440px; top: 742px; width: 100px; height: 155px; background: radial-gradient(ellipse at 55% 45%, #5b3e30, #8b7a6a 55%, rgba(255,255,255,0) 80%); }
  .badge-back { left: 105px; top: 805px; width: 105px; height: 95px; background: var(--paper); }
  .badge-back .name { font-size: 10.5px; }
  .back-band { left: 0; bottom: 0; width: 656px; height: 14px; background: var(--green); }
</style>
</head>
<body>

<article class="page page-front">
  <header class="block masthead">
    <div class="brand">
      <span class="brand-mark"></span>
      <span class="brand-name"><span class="line1">Willow Crest Avenue</span><span class="line2">Animal Clinic</span></span>
    </div>
    <div class="masthead-title">Advanced orthopedic care by Dr. Helena Pettigrew, DVM, DCCVS-SA TPLO surgery at Willow Crest Avenue Animal Clinic</div>
  </header>

  <section class="block about">
    <h2>About Dr. Helena Pettigrew</h2>
    <p>Dr. Helena Pettigrew is a board-certified veterinary surgeon (Diplomate of the Continental College of Veterinary Surgeons) with over 18 years of experience in small animal surgery. A graduate of Northgrove State University, she completed her surgical residency at Harwick School of Veterinary Medicine. Through her mobile practice, Roving Surgical Care, Dr. Pettigrew now provides advanced surgical procedures—such as TPLO—directly at local clinics.</p>
  </section>

  <section class="block what">
    <h2>What is TPLO Surgery?</h2>
    <p>Tibial Plateau Leveling Osteotomy (TPLO) is a surgical procedure that stabilizes the stifle (knee) joint following a cranial cruciate ligament (CCL) rupture—a common orthopedic injury in dogs. The procedure involves altering the angle of the tibial plateau to eliminate abnormal joint motion, restoring stability and improving function.</p>
  </section>

  <div class="block knee-illustration" role="img" aria-label="Illustration of a dog's knee joint before and after TPLO, showing the tibial plateau angle"></div>
  <div class="block radiograph" role="img" aria-label="Pre-op and post-op TPLO X-rays of a dog's stifle with measurement lines and a bone plate"></div>

  <section class="block benefits">
    <h2>Benefits of TPLO Surgery</h2>
    <div class="benefit">
      <svg viewBox="0 0 46 46"><circle cx="23" cy="23" r="21" fill="none" stroke="var(--green)" stroke-width="2.4"/><path d="M18 12c4 0 5 4 5 8s2 6 5 8c2 2 1 7-3 7M20 28c-2 2-2 5 0 7" stroke="var(--green)" stroke-width="2.2" fill="none" stroke-linecap="round"/></svg>
      <div><h3>Enhanced Joint Stability:</h3><p>Restores natural biomechanics, reducing pain and improving mobility</p></div>
    </div>
    <div class="benefit">
      <svg viewBox="0 0 46 46"><circle cx="23" cy="23" r="21" fill="none" stroke="var(--green)" stroke-width="2.4"/><circle cx="23" cy="23" r="12" stroke="var(--green)" stroke-width="2" fill="none"/><path d="M17 23l4 4 8-8" stroke="var(--green)" stroke-width="2.4" fill="none" stroke-linecap="round"/></svg>
      <div><h3>Faster Recovery:</h3><p>Many dogs return to normal activity faster compared to other surgical techniques.</p></div>
    </div>
    <div class="benefit">
      <svg viewBox="0 0 46 46"><circle cx="23" cy="23" r="21" fill="none" stroke="var(--green)" stroke-width="2.4"/><circle cx="23" cy="23" r="8" stroke="var(--green)" stroke-width="2" fill="none"/><circle cx="23" cy="23" r="13" stroke="var(--green)" stroke-width="2" stroke-dasharray="4 4" fill="none"/><path d="M19.5 23l2.5 2.5 4.5-5" stroke="var(--green)" stroke-width="2" fill="none"/></svg>
      <div><h3>TPLO is particularly effective in large and active breeds.</h3><p>TPLO is particularly effective in large and active breeds.</p></div>
    </div>
  </section>

  <section class="block why">
    <h2>Why Choose Willow Crest Avenue Animal Clinic?</h2>
    <p>Partnering with Dr. Pettigrew, Willow Crest Avenue Animal Clinic offers advanced orthopedic surgery on-site—eliminating the need for referrals or travel. This collaboration ensures your pet receives expert surgical care in a familiar, trusted environment.</p>
    <p>Our clinic works directly with your primary veterinarian to share medical records, diagnostics, and prescriptions, ensuring seamless and coordinated care for your pet.</p>
  </section>

  <div class="block pet-photo-front" role="img" aria-label="Photo of a brown puppy sitting beside a tabby kitten"></div>

  <footer class="block footer">
    <span><svg viewBox="0 0 16 16"><circle cx="8" cy="8" r="7" stroke="#fff" fill="none" stroke-width="1.3"/><ellipse cx="8" cy="8" rx="3" ry="7" stroke="#fff" fill="none" stroke-width="1.2"/><path d="M1 8h14" stroke="#fff" stroke-width="1.2"/></svg>www.brookferrypetcare.com</span>
    <span><svg viewBox="0 0 16 16"><circle cx="8" cy="8" r="7" stroke="#fff" fill="none" stroke-width="1.3"/><ellipse cx="8" cy="8" rx="3" ry="7" stroke="#fff" fill="none" stroke-width="1.2"/><path d="M1 8h14" stroke="#fff" stroke-width="1.2"/></svg>www.northgroveanimalsurgery.com</span>
  </footer>

  <div class="block surgeon-badge">
    <span class="dot"></span>
    <span class="name">Helena Pettigrew</span>
  </div>
</article>

<article class="page page-back">
  <section class="block radiograph-note">
    <h3>Diagnostic Radiographs vs. TPLO Planning Radiographs</h3>
    <p>While diagnostic radiographs may confirm a CCL tear, they are not sufficient for surgical planning. TPLO requires three advanced technique radiographic views with precise measurements, which must be performed under sedation to reduce discomfort and allow accurate positioning.</p>
  </section>

  <section class="block process">
    <h2>Expected Process</h2>
    <ol>
      <li>Diagnosis: Your pet is diagnosed with stifle instability (CCL tear) by your veterinarian.</li>
      <li>Referral: Your veterinarian contacts the surgical coordinator at Willow Crest Avenue Animal Clinic.</li>
      <li>Consultation: The coordinator contacts you to schedule a 1-hour consultation to review the procedure, estimated costs, and available surgery dates.</li>
      <li>Planning Radiographs: These specialized X-rays are typically taken during the consultation under light sedation.</li>
      <li>Surgical Review: Dr. Pettigrew reviews the radiographs and your pet's medical history to confirm candidacy for TPLO.</li>
      <li>Deposit: A $3,500 deposit secures Dr. Pettigrew's travel and surgery date. This is refundable if canceled at least 5 days prior to the scheduled procedure.</li>
      <li>Surgery Day: Your pet is dropped off in the morning and surgery is performed the same day.</li>
      <li>Discharge: You'll receive a post-surgery update and your pet will go home that evening.</li>
    </ol>
  </section>

  <section class="block followup">
    <h2>Post-Operative Care &amp; Follow-Up</h2>
    <p class="lead">Two follow-up appointments will be scheduled:</p>
    <p class="visit">4 Weeks Post-Op: Evaluate healing, refill medications, and address any questions.</p>
    <p class="visit">8 Weeks Post-Op: Sedated radiographs will confirm proper healing of the surgical site and tibia.</p>
    <p class="closing">Dr. Pettigrew will stay in direct contact with you during your pet's recovery using her custom mobile app, which allows for secure messaging and provides detailed post-operative instructions.</p>
  </section>

  <h3 class="block contact-title">Contact Information:</h3>

  <div class="block contact-card card-clinic">
    <h4>Willow Crest Avenue<br>Animal Clinic</h4>
    <p>2480 Willow Crest Avenue,<br>Fairhaven, MI 48915</p>
    <p>(517) 555-0142</p>
    <p>info@brookferrypetcare.com<br>www.brookferrypetcare.com</p>
  </div>

  <div class="block contact-card card-surgeon">
    <h4>Roving Surgical Care<br>(Dr. Helena Pettigrew)</h4>
    <p>(810) 555-0187</p>
    <p>hpettigrew@rovingsurgicalcare.com<br>www.northgroveanimalsurgery.com</p>
  </div>

  <div class="block pet-photo-back" role="img" aria-label="Photo of a brown puppy sitting beside a tabby kitten"></div>

  <div class="block surgeon-badge badge-back">
    <span class="dot"></span>
    <span class="name">Helena Pettigrew</span>
  </div>

  <div class="block back-band"></div>
</article>

</body>
</html>
```